Website for Sports and Exercise Medicine Doctor with active research in stem cells therapies.

I am a sports and exercise medicine doctor with research interests in the cutting edge areas of biological therapies, most notable stem cells. None of my patients are dying of anything, and most of them come to see me to decrease their pain, so they can get back to what they want to do.

The approach i then take is to decrease their pain and support them to achieve the things they wish to achieve. Most people start at "Just make it stop hurting doc" , but I try to move them towards something more important over time.

I would like the website to be very different to other "Doctor or medical websites" in its look. No pictures of doctors in white coats and no pictures of fit old people smiling. I would potentially like the fist thing seen to be a quote:

"Less pain. Everybody wants it, but what are you going to do, once you've got it?"

(But this is only an idea, I am open to anything)

The website will need a couple of things

1. "Locations" I work
2. "Research" I am involved in
3. "Sort Me out" - Clinical information for people to access
4. "Social" - imbedded twitter and facebook
5. "Blog" - imbedded wordpress blog
6. "Bio" - the usual bio-stuff

The "Sort Me out" - pages I would like to have the functionality as seen in this site http://www.veltarion.com.au/platelet/. I intend to put disease topics into these pages (eg Achilles tehdinopathy, osteoarthritis etc etc etc). Once again I am not wedded to this but something along these lines would be good.

To give you an idea these are some sites I like
http://www.morbanquilt.com/
http://daptrine.com/
http://ovimbera.com.sg/
http://jolvaniketchup.com/
http://www.pilnorwave.com/
http://quadrisel.com/#offering
http://fennikstudio.tv/
http://norvalgate.com/
http://sablethorn.co.uk/#about

Target Market(s)

20-80 year old.
People with tendon injuries
People with osteoarthritis
People interested in stem cells
I will build the site over time to contain information on multiple sporting injuries and musculoskeletal disorders. It will also become a site for the latest on stem cell research particularly in the area of osteoarthritis.

Industry/Entity Type

Medical

Font styles to use
Sans Serif

Colors
ffffff

Requirements
Nice to have
• To give you an idea these are some sites I like
http://daptrine.com/
http://fennikstudio.tv/
http://norvalgate.com/
Should not have
• Pictures of doctors in white coats or old fit people smiling

```html
<!DOCTYPE html>
<html lang="en">
<head>
<meta charset="utf-8">
<title>Dr Lewin Marsh – Sports and Exercise Medicine</title>
<link href="https://fonts.googleapis.com/css2?family=Arimo:wght@400;700&family=Oswald:wght@400;500&display=swap" rel="stylesheet">
<style>
:root{
  --green:#76b52a;
  --green-dark:#5f9a1c;
  --heading-green:#6aa823;
  --charcoal:#5a5758;
  --ink:#3d3d3d;
  --body:#6b6b6b;
  --rule:#d8d8d8;
  --white:#ffffff;
}
*{box-sizing:border-box;margin:0;padding:0}
html,body{width:1178px;height:1200px;overflow:hidden;background:var(--white)}
body{font-family:"Arimo",Arial,sans-serif;color:var(--ink)}
.stage{position:absolute;left:0;top:0;width:1400px;height:1426px;transform:scale(.8414);transform-origin:0 0}
.abs{position:absolute}

/* header */
.topbar{left:211px;top:0;width:980px;height:70px;background:var(--charcoal)}
.brand{left:211px;top:0;width:150px;height:116px;background:var(--charcoal);text-align:center}
.brand-mark{position:absolute;left:44px;top:14px;width:64px;height:64px;border-radius:50%;background:var(--green)}
.brand-name{position:absolute;left:0;top:80px;width:150px;font-size:19px;color:var(--white);white-space:nowrap}
.callout{right:227px;top:24px;color:var(--white);font-size:18px;display:flex;align-items:center;gap:14px}
.callout svg{width:30px;height:30px}
.mainnav{left:361px;top:70px;width:830px;height:52px;background:var(--green);display:flex;align-items:center}
.mainnav a{color:var(--white);text-decoration:none;font-size:14px;position:absolute;top:18px}

/* slider */
.hero{left:211px;top:131px;width:980px;height:442px;background:linear-gradient(160deg,#a9b8cc 0%,#5f7189 35%,#2e3a4c 60%,#93a6bd 100%)}
.hero-title{left:233px;top:393px;width:493px;height:48px;background:rgba(118,181,42,.85);color:var(--white);font-family:"Oswald",sans-serif;font-size:33px;line-height:48px;padding-left:26px;letter-spacing:.2px}
.hero-sub{left:233px;top:454px;width:873px;height:48px;background:rgba(45,45,45,.85);color:var(--white);font-family:"Oswald",sans-serif;font-size:22px;line-height:48px;padding-left:18px}
.hero-arrows{left:1123px;top:531px;display:flex;gap:2px}
.hero-arrows span{width:24px;height:24px;background:#4a4a4a;color:#ddd;font-size:13px;line-height:24px;text-align:center}

/* welcome */
.welcome-img{left:211px;top:615px;width:350px;height:197px;background:radial-gradient(circle at 50% 45%,#3a6fe0 0%,#1740a8 35%,#061330 75%,#000 100%)}
.welcome-title{left:598px;top:609px;font-size:18px;color:var(--heading-green)}
.welcome-lead{left:599px;top:642px;font-size:14px;color:var(--ink)}
.copy{font-size:11px;line-height:21px;color:var(--body)}
.welcome-copy{left:601px;top:673px;width:585px}
.btn{display:block;height:27px;border-radius:3px;background:linear-gradient(#9acd4c,#5e9a1b);color:#2f4d0c;font-size:9px;line-height:27px;text-align:center;box-shadow:0 2px 2px rgba(0,0,0,.25)}

/* columns */
.col-title{font-size:18px;font-weight:700;color:var(--heading-green);top:861px}
.col-img{top:902px;width:264px}
.col-copy{top:1080px;width:262px}
.news-item{left:843px;width:348px;height:90px}
.news-thumb{position:absolute;left:0;top:0;width:88px;height:83px}
.news-title{position:absolute;left:111px;top:0;font-size:14px;line-height:22px;color:var(--ink);width:230px}
.news-desc{position:absolute;left:111px;top:44px;width:240px}
.news-rule{left:843px;top:1001px;width:348px;height:1px;background:var(--rule)}

/* footer */
.footer{left:211px;top:1323px;width:980px;height:103px;background:var(--charcoal);color:var(--white)}
.footnav{position:absolute;left:40px;top:31px;font-size:11px;display:flex;gap:14px}
.copyright{position:absolute;left:40px;top:60px;font-size:11px}
.follow{position:absolute;left:761px;top:40px;display:flex;align-items:center;gap:5px;font-size:11px}
.follow .dot{width:29px;height:29px;border-radius:50%}
</style>
</head>
<body>
<div class="stage">

  <header>
    <div class="abs topbar"></div>
    <div class="abs brand">
      <span class="brand-mark"></span>
      <span class="brand-name">Dr Lewin Marsh</span>
    </div>
    <div class="abs callout">
      <svg viewBox="0 0 30 30" fill="none" stroke="#fff" stroke-width="3" stroke-linecap="round"><path d="M7 4c-3 3-3 8 2 14s11 9 14 6l-4-5-3 2c-2-1-5-4-6-6l2-3z" fill="#fff" stroke="none"/><path d="M18 6l6 6M24 6v6h-6"/></svg>
      <span>Call us on : +01 (0) 0220 00 202</span>
    </div>
    <nav class="abs mainnav">
      <a style="left:46px">Home</a>
      <a style="left:153px">Locations</a>
      <a style="left:283px">Research</a>
      <a style="left:413px">Sort me Out</a>
      <a style="left:558px">Social</a>
      <a style="left:666px">Blog</a>
      <a style="left:765px">Bio</a>
    </nav>
  </header>

  <section>
    <div class="abs hero" role="img" aria-label="Close-up of blue-grey neuron cells with branching fibres"></div>
    <h1 class="abs hero-title" style="font-weight:400">SPORTS AND EXERCISE MEDICINE</h1>
    <p class="abs hero-sub">DOCTOR WITH RESEARCH INTERESTS IN THE CUTTING EDGE AREAS OF BIOLOGICAL THERAPIES</p>
    <div class="abs hero-arrows"><span>&#8249;</span><span>&#8250;</span></div>
  </section>

  <section>
    <div class="abs welcome-img" role="img" aria-label="Glowing blue brain with light rays on black"></div>
    <h2 class="abs welcome-title" style="font-weight:400">WELCOME TO DR. LEWIN MARSH</h2>
    <p class="abs welcome-lead">Uncover many web sites still in their infancy. Various versions have evolved over the years</p>
    <p class="abs copy welcome-copy">It is a long established fact that a reader will be distracted by the readable content of a page when looking at its layout. The point of using Lorem Ipsum is that it has a more-or-less normal distribution of letters, as opposed to using 'Content here, content here', making it look like readable English. Many desktop publishing packages and web page editors now use Lorem Ipsum as their default model text, and a search for 'lorem ipsum' will uncover many web sites still in their infancy. Various versions have evolved over the years, sometimes by accident, sometimes on purpose.</p>
    <a class="abs btn" style="left:1083px;top:795px;width:107px">VIEW MORE INFO</a>
  </section>

  <section>
    <h3 class="abs col-title" style="left:211px">Biological Therapies</h3>
    <div class="abs col-img" style="left:211px;height:162px;background:linear-gradient(135deg,#1e6fd0,#4fb0f0 60%,#9fd6fa)" role="img" aria-label="Blue x-ray runner with heartbeat line"></div>
    <p class="abs copy col-copy" style="left:212px">It is a long established fact that a reader will be distracted by the readable content of a page when looking at its layout. The point of using Lorem Ipsum is that it has a more-or-less normal distribution of letters, as opposed to using content here is that it has a more-or-less normal distribution of letters, as opposed to using content here...</p>
    <a class="abs btn" style="left:211px;top:1244px;width:106px">VIEW MORE INFO</a>

    <h3 class="abs col-title" style="left:526px">Biological Therapies</h3>
    <div class="abs col-img" style="left:526px;height:161px;background:linear-gradient(#e4e4e4,#e4e4e4) bottom/100% 12px no-repeat,radial-gradient(circle at 40% 45%,#4d6d98 0 14%,#c81414 30%,#7a0a0a 80%)" role="img" aria-label="Virus particle among red blood cells"></div>
    <p class="abs copy col-copy" style="left:527px">It is a long established fact that a reader will be distracted by the readable content of a page when looking at its layout. The point of using Lorem Ipsum is that it has a more-or-less normal distribution of letters, as opposed to using content here is that it has a more-or-less normal distribution of letters, as opposed to using content here...</p>
    <a class="abs btn" style="left:526px;top:1244px;width:106px">VIEW MORE INFO</a>

    <h3 class="abs col-title" style="left:840px">Latest news</h3>
    <article class="abs news-item" style="top:900px">
      <div class="news-thumb" style="background:linear-gradient(135deg,#e8ecef,#9fb2bf)" role="img" aria-label="Laboratory beaker with blue liquid"></div>
      <p class="news-title">Uncover many web sites still in their infancy. Various versions...</p>
      <p class="news-desc copy">It is a long established fact that a reader will be distracted by the readable content...</p>
    </article>
    <div class="abs news-rule"></div>
    <article class="abs news-item" style="top:1016px">
      <div class="news-thumb" style="background:radial-gradient(circle at 60% 40%,#d9c067,#3b6e9a 45%,#162a44)" role="img" aria-label="Cell being injected under a microscope"></div>
      <p class="news-title">Uncover many web sites still in their infancy. Various versions...</p>
      <p class="news-desc copy">It is a long established fact that a reader will be distracted by the readable content...</p>
    </article>
    <article class="abs news-item" style="top:1136px">
      <div class="news-thumb" style="background:linear-gradient(160deg,#7aa8d6,#2d3b44 55%,#b8921e)" role="img" aria-label="Gloved hand loading sample tubes into a centrifuge"></div>
      <p class="news-title">Uncover many web sites still in their infancy. Various versions...</p>
      <p class="news-desc copy">It is a long established fact that a reader will be distracted by the readable content...</p>
    </article>
    <a class="abs btn" style="left:843px;top:1244px;width:105px">VIEW MORE NEWS</a>
  </section>

  <footer class="abs footer">
    <nav class="footnav"><span>Home</span><span>|</span><span>Locations</span><span>|</span><span>Research</span><span>|</span><span>Sort me Out</span><span>|</span><span>Social</span><span>|</span><span>Blog</span><span>|</span><span>Bio</span></nav>
    <p class="copyright">Copyright © 2013. Dr. Lewin Marsh. All rights reserved.</p>
    <div class="follow">
      <span style="margin-right:4px">Follow us :</span>
      <span class="dot" style="background:#3b6cc0"></span>
      <span class="dot" style="background:#3ba6e0"></span>
      <span class="dot" style="background:#1a8fb5"></span>
      <span class="dot" style="background:#3a3a3a"></span>
    </div>
  </footer>

</div>
</body>
</html>
```